Brindle Children's Center - Child Care brochure

I just bought a new child care and completely renovated the space. We are also designing a new website, so I need the brochure to match that with updated info. www.brindlechildrenscenter.com - Information on there is current. We expect to have the new one up and running in the next few days. We have new photo's that I'd like to be added to the flyer too. ps. the boys in the pictures are mine, so i would appreciate one of them being added :). support@pixelhutnetworks.com has details on the website (dev.brindlechildrenscenter.com). The child care program is only open during the ski season - i.e. a resort facility catering to high end clients.
I'm attaching the the website information, the flyer I created, logo files and pictures.

Target Market(s)

Parents of young children

Font styles to use
Other font styles liked:
• "Things we said" & "Calibri Light"

Colors
cfeae6
fef1ee

Requirements
Must have
• Pictures of children. sleek design - winter, mountain theme. Check with website designer on new website.
Nice to have
• prices included
Should not have
• Kid like artwork

```html
<!DOCTYPE html>
<html lang="en">
<head>
<meta charset="utf-8">
<title>Brindle Children's Center – Brochure</title>
<link href="https://fonts.googleapis.com/css2?family=Amatic+SC:wght@700&family=Lato:wght@300;400;700&display=swap" rel="stylesheet">
<style>
  :root{
    --bg:#3a3a3a;
    --teal:#8ed0c6;
    --teal-deep:#7cc2b7;
    --teal-soft:#a9dcd4;
    --salmon:#ee8a76;
    --ink:#3c3c3c;
    --white:#ffffff;
    --snow:#dfe6f2;
    --sky:#b9c6e6;
  }
  *{box-sizing:border-box;margin:0;padding:0}
  html,body{width:1200px;height:1200px;overflow:hidden;background:var(--bg);font-family:'Lato',sans-serif;color:var(--ink)}
  .brochure{position:absolute;left:50px;top:175px;width:1100px;height:850px;display:flex;box-shadow:0 20px 50px rgba(0,0,0,.45)}
  .panel{position:relative;width:366.67px;height:850px;overflow:hidden}
  .panel svg.bg{position:absolute;inset:0}

  /* inner text panel */
  .panel--intro{background:var(--white)}
  .intro-copy{position:absolute;left:26px;right:26px;top:362px;font-size:11px;line-height:1.32;font-weight:400}
  .tag{display:inline-block;background:var(--salmon);color:var(--white);font-size:11px;padding:4px 18px 4px 26px;margin:0 0 10px -26px;clip-path:polygon(0 0,100% 0,92% 100%,0 100%)}
  .intro-copy p{margin-bottom:12px;text-align:justify}
  .activities{display:grid;grid-template-columns:1fr 1fr;gap:6px 10px;list-style:none;margin-top:14px}
  .activities li{display:flex;align-items:flex-start;gap:6px;font-size:11px;line-height:1.25}
  .tick{flex:none;width:12px;height:12px;margin-top:1px}

  /* contact panel */
  .panel--contact{background:var(--teal)}
  .contact{position:absolute;left:0;right:0;top:260px;text-align:center;color:var(--white);font-size:12.5px;line-height:1.35}
  .brand-mark{width:110px;height:110px;border-radius:50%;background:var(--white);margin:0 auto 22px;display:flex;align-items:center;justify-content:center;text-align:center;color:var(--ink);font-weight:700;font-size:12px;line-height:1.2;padding:12px}
  .contact h2{font-size:13px;font-weight:700;letter-spacing:.3px;margin-bottom:14px}
  .contact .icon{width:16px;height:16px;display:block;margin:0 auto 4px}
  .contact .item{margin-bottom:16px}
  .hours{display:inline-block;background:var(--teal-deep);border-radius:12px;padding:3px 16px;font-weight:700;margin:4px 0 12px}
  .contact .note{margin-bottom:16px}
  .url{position:absolute;left:0;right:0;bottom:26px;text-align:center;color:var(--white);font-size:11px;letter-spacing:2px}

  /* cover panel */
  .panel--cover{background:var(--white)}
  .cover-name{position:absolute;top:34px;left:0;right:0;display:flex;align-items:center;justify-content:center;gap:8px;font-weight:700;font-size:14px;color:var(--ink)}
  .cover-name .dot{width:14px;height:14px;border-radius:50%;background:var(--ink)}
  .welcome{position:absolute;left:50px;right:14px;top:600px;text-align:center;color:var(--white);font-family:'Amatic SC',cursive}
  .welcome .line1{font-size:50px;line-height:1}
  .welcome .line2{font-size:30px;line-height:1.1;margin-top:8px}
  .panel--cover .url{left:40px;bottom:36px;font-size:10px}
</style>
</head>
<body>
<main class="brochure">

  <section class="panel panel--intro">
    <svg class="bg" width="367" height="850" viewBox="0 0 367 850">
      <path role="img" aria-label="Photo of a toddler reading a picture book beside a large teddy bear" d="M0 0 H330 C350 90 340 220 250 290 C180 330 80 335 0 320 Z" fill="#c9b08e"/>
      <path d="M330 0 C350 90 340 220 250 290 C180 330 80 335 0 320" fill="none" stroke="var(--salmon)" stroke-width="6"/>
      <path d="M342 0 C362 95 352 230 258 300 C185 342 80 347 0 332" fill="none" stroke="var(--salmon)" stroke-width="2"/>
    </svg>
    <div class="intro-copy">
      <span class="tag">Welcome to the Brindle Children's Center!</span>
      <p>When you hit the slopes you want to make sure your child has a great day too. At the Brindle Children's Center you can be sure that your child receives the best care possible – and has a great time to boot! Located on the slopes of world famous Brindle Ski Resort, you can drop off your child at a safe, and fun center and step out the door to the slopes.</p>
      <span class="tag">Our Services</span>
      <p>The Brindle Children's Center is a full service childcare facility that caters to children from six weeks to nine years old. Infants, toddlers, and young children can explore the activities and toys available in the Center. Children ages four and older have the option to join Brindle's legendary Halvor Berg Ski School and spend part or all of the day learning from one of Brindle's friendly instructors.</p>
      <p>Children visiting the center can look forward to the following activities:</p>
      <ul class="activities">
        <li><svg class="tick" viewBox="0 0 14 14"><circle cx="7" cy="7" r="6" fill="none" stroke="var(--salmon)" stroke-width="1.4"/><path d="M4 7.2l2 2 4-4.4" fill="none" stroke="var(--salmon)" stroke-width="1.6"/></svg>Dramatic play</li>
        <li><svg class="tick" viewBox="0 0 14 14"><circle cx="7" cy="7" r="6" fill="none" stroke="var(--salmon)" stroke-width="1.4"/><path d="M4 7.2l2 2 4-4.4" fill="none" stroke="var(--salmon)" stroke-width="1.6"/></svg>Games</li>
        <li><svg class="tick" viewBox="0 0 14 14"><circle cx="7" cy="7" r="6" fill="none" stroke="var(--salmon)" stroke-width="1.4"/><path d="M4 7.2l2 2 4-4.4" fill="none" stroke="var(--salmon)" stroke-width="1.6"/></svg>Arts and Crafts</li>
        <li><svg class="tick" viewBox="0 0 14 14"><circle cx="7" cy="7" r="6" fill="none" stroke="var(--salmon)" stroke-width="1.4"/><path d="M4 7.2l2 2 4-4.4" fill="none" stroke="var(--salmon)" stroke-width="1.6"/></svg>Music</li>
        <li><svg class="tick" viewBox="0 0 14 14"><circle cx="7" cy="7" r="6" fill="none" stroke="var(--salmon)" stroke-width="1.4"/><path d="M4 7.2l2 2 4-4.4" fill="none" stroke="var(--salmon)" stroke-width="1.6"/></svg>Discovery Science</li>
        <li><svg class="tick" viewBox="0 0 14 14"><circle cx="7" cy="7" r="6" fill="none" stroke="var(--salmon)" stroke-width="1.4"/><path d="M4 7.2l2 2 4-4.4" fill="none" stroke="var(--salmon)" stroke-width="1.6"/></svg>Nutritious lunch and snacks</li>
        <li><svg class="tick" viewBox="0 0 14 14"><circle cx="7" cy="7" r="6" fill="none" stroke="var(--salmon)" stroke-width="1.4"/><path d="M4 7.2l2 2 4-4.4" fill="none" stroke="var(--salmon)" stroke-width="1.6"/></svg>Snow Play</li>
      </ul>
    </div>
  </section>

  <section class="panel panel--contact">
    <svg class="bg" width="367" height="850" viewBox="0 0 367 850">
      <defs>
        <linearGradient id="faint-photo" x1="0" y1="0" x2="0" y2="1">
          <stop offset="0" stop-color="var(--teal-soft)" stop-opacity=".7"/>
          <stop offset="1" stop-color="var(--teal)" stop-opacity="0"/>
        </linearGradient>
      </defs>
      <rect role="img" aria-label="Faded background photo of two children playing" x="0" y="0" width="367" height="420" fill="url(#faint-photo)"/>
    </svg>
    <div class="contact">
      <div class="brand-mark">Brindle Children's Center</div>
      <h2>BRINDLE CHILDREN'S CENTER</h2>
      <div class="item">
        <svg class="icon" viewBox="0 0 16 16"><path d="M1 8L8 2l7 6h-2v6H10v-4H6v4H3V8z" fill="var(--white)"/></svg>
        P.O. Box 4127<br>Brindle, Utah 84310
      </div>
      <div class="item">
        <svg class="icon" viewBox="0 0 16 16"><circle cx="8" cy="8" r="7" fill="none" stroke="var(--white)" stroke-width="1.2"/><path d="M5.5 4.5l1.5 1-.7 1.3c.6 1.2 1.4 2 2.6 2.6l1.3-.7 1 1.5-1.2 1.2C8 11 5 8 4.3 5.7z" fill="var(--white)"/></svg>
        (801) 555-0186
      </div>
      <div class="item">
        <svg class="icon" viewBox="0 0 16 16"><rect x="1.5" y="4" width="13" height="9" rx="1" fill="var(--white)"/><path d="M1.5 4.5L8 9l6.5-4.5" fill="none" stroke="var(--teal)" stroke-width="1.2"/></svg>
        info@brindlechildrenscenter.com
      </div>
      <span class="hours">Open daily: 8:30-4:30</span>
      <p class="note">Serving children ages<br>6 wks thru 9 years</p>
      <p class="note">(Located at the Summit Ticket<br>Office Building)</p>
    </div>
    <div class="url">www.brindlechildrenscenter.com</div>
  </section>

  <section class="panel panel--cover">
    <svg class="bg" width="367" height="850" viewBox="0 0 367 850">
      <defs>
        <linearGradient id="mountain" x1="0" y1="0" x2="0" y2="1">
          <stop offset="0" stop-color="var(--white)"/>
          <stop offset=".25" stop-color="var(--sky)"/>
          <stop offset=".6" stop-color="#8c8f98"/>
          <stop offset="1" stop-color="var(--snow)"/>
        </linearGradient>
      </defs>
      <rect role="img" aria-label="Photo of the lodge beneath snowy mountain slopes with skiers" x="0" y="0" width="367" height="480" fill="url(#mountain)"/>
      <path d="M0 540 C80 440 220 400 367 380 V850 H0 Z" fill="var(--white)"/>
      <path d="M30 850 C10 720 50 600 160 552 C240 520 320 522 367 532 V850 Z" fill="var(--teal)"/>
      <path d="M20 850 C0 720 40 595 150 545" fill="none" stroke="var(--salmon)" stroke-width="4"/>
      <circle cx="110" cy="460" r="50" fill="var(--white)" stroke="var(--teal)" stroke-width="5"/>
      <circle role="img" aria-label="Photo of a toddler playing indoors" cx="110" cy="460" r="42" fill="#c7a98a"/>
      <circle cx="240" cy="445" r="60" fill="var(--white)" stroke="var(--teal)" stroke-width="5"/>
      <circle role="img" aria-label="Photo of a toddler playing with a toy" cx="240" cy="445" r="51" fill="#b99a74"/>
    </svg>
    <div class="cover-name"><span class="dot"></span>Brindle Children's Center</div>
    <div class="welcome">
      <div class="line1">Welcome to</div>
      <div class="line2">Brindle Children's Center!</div>
    </div>
    <div class="url">www.brindlechildrenscenter.com</div>
  </section>

</main>
</body>
</html>
```